Business Card Re-Design for a Lighting Designer

I would like my business card re-designed. It is currently high gloss and they scratch too easily. I don not think the current design lends itself well to a matte finish. I have included the current design for reference along with our company logo.
Check out our website for current branding.
http://www.brambleorchidstudio.example

Updates
Some of the top contenders are muslim and it is a holiday for them. I do not want to discriminate and would expect the same courtesy for holidays we celebrate.
Target Market(s)
Interior Designers, Architects
Contact Information for Business Card
Logo - Name, Title, Address, Telephone Number and Extension, Email
Font styles to use
Requirements
Must have
- All the information listed on the current business card. If you use Red, it needs to be the red from our logo.
Nice to have
- Vertical and Horizontal Designs will be entertained.
Should not have
- Requirements for a glossy finish...should not look too corporate since we are a design firm.

```html
<!DOCTYPE html>
<html lang="en">
<head>
<meta charset="utf-8">
<title>Bramble Orchid Studio — Business Card</title>
<link href="https://fonts.googleapis.com/css2?family=Montserrat:wght@300;400;500;700&display=swap" rel="stylesheet">
<style>
  :root {
    --backdrop: #3a3b3d;
    --ink-black: #0c0c0c;
    --band-black: #1b1b1c;
    --brand-red: #a3151b;
    --paper: #ffffff;
    --grey-text: #8a8a8a;
    --soft-white: #f2f2f2;
    --card-w: 360px;
    --card-h: 600px;
  }
  * { box-sizing: border-box; margin: 0; padding: 0; }
  html, body { width: 1200px; height: 900px; overflow: hidden; }
  body {
    background: var(--backdrop);
    font-family: "Montserrat", "Helvetica Neue", Arial, sans-serif;
    display: flex;
    align-items: center;
    justify-content: center;
    gap: 110px;
  }
  .card {
    width: var(--card-w);
    height: var(--card-h);
    position: relative;
    overflow: hidden;
    box-shadow: 0 14px 34px rgba(0,0,0,0.45);
  }

  /* Brand lockup */
  .brand {
    display: flex;
    flex-direction: column;
    align-items: center;
    text-align: center;
  }
  .brand-square {
    width: 64px;
    height: 64px;
    background: var(--brand-red);
    margin-bottom: 22px;
  }
  .brand-name {
    font-weight: 300;
    font-size: 34px;
    line-height: 1.05;
    letter-spacing: 0.5px;
  }
  .brand-rule {
    width: 250px;
    height: 2px;
    background: var(--brand-red);
    margin: 14px 0 8px;
  }
  .brand-tagline {
    font-weight: 500;
    font-size: 12px;
    letter-spacing: 1.6px;
    color: var(--grey-text);
  }

  /* Front */
  .card-front { background: var(--ink-black); display: flex; align-items: center; justify-content: center; }
  .card-front .brand-name { color: var(--soft-white); }
  .card-front .brand-tagline { color: #b0b0b0; }

  /* Back */
  .card-back { background: var(--brand-red); }
  .back-top {
    background: var(--paper);
    height: 268px;
    display: flex;
    align-items: center;
    justify-content: center;
    padding-top: 6px;
  }
  .card-back .brand-square { width: 52px; height: 52px; margin-bottom: 16px; }
  .card-back .brand-name { color: #4a4a4a; font-size: 29px; }
  .card-back .brand-rule { width: 220px; margin: 11px 0 6px; background: #d98a6e; }
  .card-back .brand-tagline { font-size: 10.5px; }

  .name-band {
    margin-top: 20px;
    background: var(--band-black);
    height: 64px;
    display: flex;
    align-items: center;
    justify-content: center;
  }
  .person-name {
    color: var(--soft-white);
    font-weight: 400;
    font-size: 28px;
    letter-spacing: 0.5px;
  }
  .person-title {
    margin-top: 12px;
    text-align: center;
    color: var(--soft-white);
    font-weight: 700;
    font-size: 14px;
    letter-spacing: 3px;
  }
  .contact {
    margin-top: 26px;
    text-align: center;
    color: var(--soft-white);
    font-weight: 400;
    font-size: 14.5px;
    line-height: 1.45;
  }
  .contact p + p { margin-top: 12px; }
  .website {
    margin-top: 18px;
    text-align: center;
    color: var(--soft-white);
    font-weight: 700;
    font-size: 14px;
  }
</style>
</head>
<body>
  <section class="card card-front" aria-label="Card front">
    <div class="brand">
      <div class="brand-square"></div>
      <div class="brand-name">BRAMBLE<br>ORCHID STUDIO</div>
      <div class="brand-rule"></div>
      <div class="brand-tagline">LIGHTING FOR ARCHITECTURE</div>
    </div>
  </section>

  <section class="card card-back" aria-label="Card back">
    <div class="back-top">
      <div class="brand">
        <div class="brand-square"></div>
        <div class="brand-name">BRAMBLE<br>ORCHID STUDIO</div>
        <div class="brand-rule"></div>
        <div class="brand-tagline">LIGHTING FOR ARCHITECTURE</div>
      </div>
    </div>
    <div class="name-band">
      <h1 class="person-name">MAREN ASHCOMBE</h1>
    </div>
    <div class="person-title">- PRINCIPAL -</div>
    <div class="contact">
      <p>212 Linden Crossing Way, Suite 140<br>Marlow, Oregon 97301 USA</p>
      <p>maren@brambleorchidstudio.example<br>555.014.2270 x1</p>
    </div>
    <div class="website">www.brambleorchidstudio.example</div>
  </section>
</body>
</html>
```